Mobile welding fabrication and repair, heavy equipment and semi repair

We need a business card design that will catch the eye but look prelesional at the same time. Were based out of Idaho and we do all welding fabrication jobs and repairs, we also build and install custom pipe fences for personal or larger scale fence jobs and can give free quotes. We can do semi truck and trailer repairs Mobily also.

Target Market(s)

Welding

Industry/Entity Type

welding and repair

Contact Information for Business Card

email (lanternforgeandfix@mailbay.net, phone number 208-471-3862, owner (Dalton Venkroff), Pipe Fence, Semi Repair, Mobile welding and fabrication

Font styles to use
Sans Serif

Requirements
Must have
• My logo in black background on one side , and other side my logo in white back round with all the information listed on card details
Nice to have
• make it stand out from other business cards

```html
<!DOCTYPE html>
<html lang="en">
<head>
<meta charset="UTF-8">
<title>Lantern Forge and Fix – Business Card</title>
<link href="https://fonts.googleapis.com/css2?family=Lato:wght@400;700;900&display=swap" rel="stylesheet">
<style>
  :root {
    --stage: #2a2a2a;
    --card-black: #0d0d0d;
    --card-white: #ffffff;
    --brand-blue: #1a7fd1;
    --text-light: #f2f2f2;
  }
  * { box-sizing: border-box; margin: 0; padding: 0; }
  html, body {
    width: 1200px; height: 1015px; overflow: hidden;
    background: var(--stage);
    font-family: "Lato", Arial, sans-serif;
  }
  .card {
    position: absolute; left: 250px; width: 700px; height: 400px;
    overflow: hidden; box-shadow: 0 14px 36px rgba(0,0,0,.55);
  }
  .card--front { top: 60px; background: var(--card-black); }
  .card--back { top: 555px; background: var(--card-white); }

  .brand-name {
    font-weight: 900; color: var(--brand-blue);
    text-transform: uppercase; letter-spacing: 2px; line-height: 1.08;
  }
  .card--front .brand-name {
    position: absolute; left: 0; right: 0; top: 110px;
    text-align: center; font-size: 44px;
  }
  .services {
    position: absolute; left: 0; right: 0; bottom: 70px;
    display: flex; justify-content: center; align-items: center; gap: 12px;
    color: var(--text-light); font-size: 15px; letter-spacing: 1px; text-transform: uppercase;
  }
  .services__dot {
    width: 8px; height: 8px; border-radius: 50%; background: var(--brand-blue);
  }

  .wave { position: absolute; inset: 0; }
  .card--back .brand-name {
    position: absolute; left: 50px; top: 85px; font-size: 34px;
  }
  .contact {
    position: absolute; right: 40px; top: 168px; text-align: right;
  }
  .contact__name {
    color: var(--brand-blue); font-size: 22px; font-weight: 700;
    text-transform: uppercase; letter-spacing: .5px;
  }
  .contact__role {
    color: var(--text-light); font-size: 15px; letter-spacing: 1px; margin-top: 2px;
  }
  .contact__line {
    display: flex; justify-content: flex-end; align-items: center; gap: 10px;
    color: var(--text-light); font-size: 16px; margin-top: 10px;
  }
  .contact__line--phone { margin-top: 30px; }
  .contact__line svg { width: 17px; height: 17px; fill: var(--brand-blue); }
</style>
</head>
<body>
  <section class="card card--front">
    <div class="brand-name">Lantern<br>Forge and Fix</div>
    <div class="services">
      <span>Fabrication</span><span class="services__dot"></span>
      <span>Mobile Welding</span><span class="services__dot"></span>
      <span>Semi Repair</span><span class="services__dot"></span>
      <span>Pipe Fence</span>
    </div>
  </section>

  <section class="card card--back">
    <svg class="wave" viewBox="0 0 700 400" preserveAspectRatio="none">
      <path d="M0,278 C170,290 270,250 360,160 C450,70 530,52 640,55"
            fill="none" stroke="#1a7fd1" stroke-width="7"/>
      <path d="M0,300 C180,306 290,268 385,170 C470,85 545,64 655,60"
            fill="none" stroke="#0d0d0d" stroke-width="7"/>
      <path d="M0,318 C190,322 305,286 405,185 C490,100 560,75 700,72 L700,400 L0,400 Z"
            fill="#0d0d0d"/>
    </svg>
    <div class="brand-name">Lantern<br>Forge and Fix</div>
    <div class="contact">
      <div class="contact__name">Dalton Venkroff</div>
      <div class="contact__role">OWNER</div>
      <div class="contact__line contact__line--phone">208-471-3862
        <svg viewBox="0 0 24 24"><path d="M6.6 10.8a15 15 0 0 0 6.6 6.6l2.2-2.2c.3-.3.7-.4 1-.2 1.1.4 2.3.6 3.6.6.6 0 1 .4 1 1V20c0 .6-.4 1-1 1A17 17 0 0 1 3 4c0-.6.4-1 1-1h3.5c.6 0 1 .4 1 1 0 1.3.2 2.5.6 3.6.1.3 0 .7-.2 1z"/></svg>
      </div>
      <div class="contact__line">lanternforgeandfix@mailbay.net
        <svg viewBox="0 0 24 24"><path d="M2 5h20v14H2V5zm2 2v.5l8 5 8-5V7H4z"/></svg>
      </div>
    </div>
  </section>
</body>
</html>
```